Upgrade Existing Web Design for an Investments Firm

We need a web designer for a company based in Dubai called Harborline Capital. We have an existing website which needs certain additions and changes. The design should be similar to typical corporate finance company websites. We're providing you with the link of our current website below - http://harborlinegroup-example.ae/
We would require the mock-ups to be ready in c. 7 working days and another 7 working days for the coding implementation. Timeline and promp response is very important for us as a client.

Target Market(s)

Investors/Consumer Brands/Financial Service Institutions/ Job Seekers

Industry/Entity Type

Financial Service

Coding

Coded - Design and coding required

Number of Pages Required

5+ page

Font styles to use
Other font styles liked:
• Arial

Colors
f04a51
000000
919191
cbcbcb

Requirements
Nice to have
• It should be similar to https://www.corvexaholdings-example.com
• Mobile Optimised as well

```html
<!DOCTYPE html>
<html lang="en">
<head>
<meta charset="utf-8">
<title>Harborline Capital</title>
<link href="https://fonts.googleapis.com/css2?family=Arimo:ital,wght@0,400;0,700;1,700&family=Roboto:wght@300;400;500&display=swap" rel="stylesheet">
<style>
:root{
  --red:#f04a51;
  --black:#000000;
  --grey:#919191;
  --light:#cbcbcb;
  --ink:#333333;
  --topbar:#1b1b1b;
  --footer:#1c1c1c;
  --soft:#f7f7f7;
  --field:#f2f2f2;
}
*{box-sizing:border-box;margin:0;padding:0}
html,body{width:1200px;height:2894px;overflow:hidden}
body{font-family:"Roboto",Arial,sans-serif;color:var(--ink);background:#fff;position:relative}
.wrap{width:1030px;margin:0 auto;position:relative}
.topbar{height:52px;background:var(--topbar);color:#9a9a9a;font-size:13px}
.topbar .wrap{display:flex;align-items:center;height:52px}
.topbar .right{margin-left:auto;display:flex;gap:46px}
.topbar .item{display:flex;align-items:center;gap:14px}
.header{height:96px;background:var(--black)}
.header .wrap{display:flex;align-items:center;height:96px}
.brand{display:flex;align-items:center;gap:12px;color:#fff;font-size:24px;font-weight:500;letter-spacing:1px}
.brand i{width:34px;height:34px;background:var(--red);display:block}
.social{margin-left:auto;display:flex;gap:14px}
.social i{width:34px;height:34px;border-radius:50%;background:#3a3a3a;display:block}
.nav{height:52px;background:linear-gradient(#ffffff,#e6e6e6);border-bottom:1px solid #ddd}
.nav .wrap{display:flex;align-items:center;height:52px;font-size:13px;color:#222}
.nav a{text-decoration:none;color:inherit;margin-right:58px}
.nav a.active{color:var(--red)}
.nav .search{margin-left:auto}
.hero{height:620px;position:relative;background:linear-gradient(160deg,#6d7a8d 0%,#3b4453 40%,#1e232c 100%)}
.hero .copy{position:absolute;top:222px;left:0;right:0;text-align:center;color:#fff;font-family:"Arimo",Arial,sans-serif}
.hero h1{font-size:32px;font-style:italic;font-weight:700;margin-left:50px}
.hero p{font-size:23px;margin-top:2px;margin-left:50px}
.hero .btn{display:inline-block;margin-top:30px;margin-left:50px;border:1px solid rgba(255,255,255,.6);padding:14px 38px;font-size:13px;color:#fff}
.dots{position:absolute;top:540px;left:565px;display:flex;gap:8px}
.dots i{width:16px;height:16px;border-radius:50%;border:2px solid #fff;display:block}
.dots i.on{background:var(--red)}
.about{height:357px;background:#fafafa;text-align:center;padding-top:62px;border-bottom:1px solid #eee}
.title{font-size:29px;font-weight:300;color:#222}
.title:after{content:"";display:block;width:36px;height:3px;background:var(--red);margin:14px auto 0}
.about p{width:880px;margin:36px auto 0;font-size:13px;line-height:19px;color:var(--grey)}
.btn-red{display:inline-block;background:var(--red);color:#fff;font-size:13px;padding:10px 22px;margin-top:34px}
.features{height:459px;padding-top:86px}
.features .grid{display:grid;grid-template-columns:532px 498px;row-gap:48px}
.feature{display:flex;gap:16px}
.feature .icon{width:62px;height:62px;background:var(--red);flex:none;display:flex;align-items:center;justify-content:center}
.feature h3{font-size:16px;font-weight:400;color:#333;margin:-4px 0 8px}
.feature p{font-size:12px;line-height:16px;color:var(--grey);width:400px;margin-bottom:10px}
.news{height:434px;background:var(--soft);padding-top:64px;border-top:1px solid #eee}
.news .wrap{display:flex}
.list{width:343px}
.list .tab{background:var(--red);color:#fff;font-size:19px;padding:9px 30px}
.list .entry{margin-left:16px;padding:22px 0;border-bottom:1px solid #ddd;font-size:12px;color:var(--grey)}
.date{display:flex;align-items:center;gap:8px;font-size:13px;color:var(--grey)}
.list .entry p{margin:14px 0 10px;line-height:16px;width:280px}
.more{font-size:10px;color:#222;display:flex;align-items:center;gap:18px;font-weight:500}
.card{width:307px}
.card .photo{height:203px;margin-top:14px}
.card h4{font-size:19px;font-weight:400;color:#111;text-align:center;margin-top:16px;line-height:25px}
.contact{height:534px;padding-top:72px}
.contact .title{text-align:center}
.contact .cols{display:flex;margin-top:70px}
.info{width:520px}
.info .row{display:flex;gap:34px;padding:0 0 24px 52px;margin-bottom:24px;border-bottom:1px solid #e3e3e3;font-size:21px;color:#333;line-height:27px}
.info .row:last-child{border:none}
.form{margin-left:124px;width:407px}
.form div{background:var(--field);height:50px;margin-bottom:8px;font-size:12px;color:#aaa;padding:18px 28px}
.form div.msg{height:96px}
.form .send{float:right;background:var(--red);color:#fff;font-size:15px;width:134px;height:42px;text-align:center;line-height:42px;margin-top:14px}
.footer{height:290px;background:var(--footer);text-align:center;color:#bbb}
.footer .copy{padding-top:48px;font-size:15px}
.footer .links{display:flex;justify-content:center;gap:92px;margin-top:42px;color:#fff;font-size:16px;font-weight:500}
.footer .icons{display:flex;justify-content:center;gap:14px;margin-top:44px}
.footer .icons i{width:46px;height:46px;border-radius:50%;background:#3c3c3c;display:block}
</style>
</head>
<body>
<div class="topbar"><div class="wrap">
  <span class="item"><svg width="12" height="16" viewBox="0 0 12 16"><path d="M6 0a6 6 0 0 0-6 6c0 4.5 6 10 6 10s6-5.5 6-10a6 6 0 0 0-6-6zm0 8.5A2.5 2.5 0 1 1 6 3.5a2.5 2.5 0 0 1 0 5z" fill="#777"/></svg>Office 1407, Seabrook Plaza Office Tower, Dubai, UAE</span>
  <div class="right">
    <span class="item"><svg width="14" height="14" viewBox="0 0 14 14"><path d="M3 0l3 3-2 2c1 2 3 4 5 5l2-2 3 3-2 3C6 14 0 8 0 3z" fill="#777"/></svg>0097145550182</span>
    <span class="item"><svg width="16" height="12" viewBox="0 0 16 12"><rect width="16" height="12" fill="#777"/><path d="M0 0l8 6 8-6" stroke="#1b1b1b" fill="none"/></svg>info@harborlinegroup-example.ae</span>
  </div>
</div></div>
<header class="header"><div class="wrap">
  <div class="brand"><i></i>Harborline Capital</div>
  <div class="social"><i></i><i></i><i></i></div>
</div></header>
<nav class="nav"><div class="wrap">
  <a class="active">Home</a><a>About</a><a>Our Approach</a><a>Portfolio</a><a>Our People</a><a>Contact</a>
  <svg class="search" width="24" height="24" viewBox="0 0 24 24"><circle cx="10" cy="10" r="8" stroke="#777" stroke-width="2" fill="none"/><path d="M16 16l7 7" stroke="#777" stroke-width="2"/></svg>
</div></nav>
<section class="hero" role="img" aria-label="Upward view of glass office towers against a pale sky">
  <div class="copy">
    <h1>Harborline Partners &amp; Co is the #1</h1>
    <p>specialist retail and consumer products investment firm in GCC</p>
    <span class="btn">READ MORE</span>
  </div>
  <div class="dots"><i class="on"></i><i></i><i></i></div>
</section>
<section class="about">
  <h2 class="title">About Us</h2>
  <p>Harborline Partners &amp; Co ("HPC") is an investment and management firm providing growth capital to global emerging brands in the consumer sector which target to enter the GCC. HPC operates under commercial license 518730 and its business activities comprise investment and management across multi sectors, including retail and consumer products. The firm has been incorporated in Dubai in July 2016.</p>
  <span class="btn-red">READ MORE</span>
</section>
<section class="features"><div class="wrap grid">
  <div class="feature">
    <div class="icon"><svg width="34" height="34" viewBox="0 0 34 34" fill="#fff"><rect x="5" y="6" width="24" height="26"/><rect x="3" y="3" width="28" height="4"/><g fill="#f04a51"><rect x="9" y="11" width="4" height="4"/><rect x="15" y="11" width="4" height="4"/><rect x="21" y="11" width="4" height="4"/><rect x="9" y="18" width="4" height="4"/><rect x="21" y="18" width="4" height="4"/><rect x="14" y="24" width="6" height="8"/></g></svg></div>
    <div><h3>Specialist Venture Capital Firm</h3>
    <p>HCL's specializes in providing growth capital to emerging brands operating in retail and consumer products sector.</p>
    <p>We partner with established brands/franchises with a track record in operations and international expansion</p></div>
  </div>
  <div class="feature">
    <div class="icon"><svg width="34" height="34" viewBox="0 0 34 34" fill="none" stroke="#fff" stroke-width="2"><circle cx="12" cy="10" r="7"/><path d="M12 6v8M10 8h4M10 12h4"/><path d="M4 32c0-6 4-10 8-10s8 4 8 10"/><path d="M22 16h8M26 12l4 4-4 4"/></svg></div>
    <div><h3>Experienced Investment Advisor</h3>
    <p>The firm is a growth capital investor with deep expertise in SME advisory, specializing in growth funding model</p>
    <p>HCL operates a fully fledged investment advisory team which provides strategy and corporate development consulting services internally and externally</p></div>
  </div>
  <div class="feature">
    <div class="icon"><svg width="34" height="34" viewBox="0 0 34 34" fill="#fff"><rect x="4" y="22" width="5" height="10"/><rect x="12" y="17" width="5" height="15"/><rect x="20" y="20" width="5" height="12"/><rect x="28" y="12" width="4" height="20"/><path d="M3 16l9-8 7 5 10-9" stroke="#fff" stroke-width="2" fill="none"/></svg></div>
    <div><h3>Fast Growing Portfolio</h3>
    <p>Harborline Capital partnered with VELTRO Footwear in July 2016 and introduced the sneaker concept in GCC, Levant, India, Egypt, Iran and Nigeria amongst others</p>
    <p>VELTRO franchise, successfully developed by HCL has enabled the concept to expand in UAE, Saudi Arabia, Lebanon and Nigeria since 2016</p></div>
  </div>
  <div class="feature">
    <div class="icon"><svg width="36" height="34" viewBox="0 0 36 34" fill="#fff"><circle cx="18" cy="10" r="5"/><circle cx="7" cy="13" r="4"/><circle cx="29" cy="13" r="4"/><path d="M10 30c0-6 3-11 8-11s8 5 8 11z"/><path d="M1 30c0-5 2-9 6-9s5 3 5 3l-1 6zM35 30c0-5-2-9-6-9s-5 3-5 3l1 6z"/></svg></div>
    <div><h3>Outstanding Team of Professionals</h3>
    <p>The founder, Mira Solvane brings extensive experience in venture capital and private equity in GCC across fundraising, investment and exit</p>
    <p>HCL is supported by an outstanding group of shareholders, independent board members and a dedicated team of investment professionals and retail specialists</p></div>
  </div>
</div></section>
<section class="news"><div class="wrap">
  <div class="list">
    <div class="tab">In the news</div>
    <div class="entry"><span class="date"><svg width="14" height="14"><circle cx="7" cy="7" r="6" stroke="#919191" fill="none"/><path d="M7 3v4h3" stroke="#919191" fill="none"/></svg>26 Feb, 2017</span>
      <p>Harborline Partners partners with global retail brand VELTRO Footwear ...</p>
      <span class="more">READ FULL ARTICLE <svg width="16" height="8"><path d="M0 4h14M11 1l3 3-3 3" stroke="#222" fill="none"/></svg></span></div>
    <div class="entry"><span class="date"><svg width="14" height="14"><circle cx="7" cy="7" r="6" stroke="#919191" fill="none"/><path d="M7 3v4h3" stroke="#919191" fill="none"/></svg>26 Feb, 2017</span>
      <p>Harborline Partners partners with global retail brand VELTRO Footwear ...</p>
      <span class="more">READ FULL ARTICLE <svg width="16" height="8"><path d="M0 4h14M11 1l3 3-3 3" stroke="#222" fill="none"/></svg></span></div>
  </div>
  <article class="card" style="margin-left:40px">
    <span class="date"><svg width="14" height="14"><circle cx="7" cy="7" r="6" stroke="#919191" fill="none"/><path d="M7 3v4h3" stroke="#919191" fill="none"/></svg>26 Feb, 2017</span>
    <div class="photo" role="img" aria-label="Person in ripped jeans and sneakers seated on a concrete ledge" style="background:linear-gradient(180deg,#a7b3bd,#8a8f93 55%,#9a9590)"></div>
    <h4>Key insights for retail sector<br>in GCC</h4>
  </article>
  <article class="card" style="margin-left:29px">
    <span class="date"><svg width="14" height="14"><circle cx="7" cy="7" r="6" stroke="#919191" fill="none"/><path d="M7 3v4h3" stroke="#919191" fill="none"/></svg>26 Feb, 2017</span>
    <div class="photo" role="img" aria-label="Blurred person holding up a red winner badge" style="background:linear-gradient(135deg,#c9c2b8,#9c8a7a 50%,#c8c4bc)"></div>
    <h4>Omni-channel as market entry<br>strategy</h4>
  </article>
</div></section>
<section class="contact"><div class="wrap">
  <h2 class="title">Contact Us</h2>
  <div class="cols">
    <div class="info">
      <div class="row"><svg width="22" height="26" viewBox="0 0 22 26"><path d="M5 1l4 6-3 3c1 3 4 7 7 8l3-3 5 4-3 5C8 24 0 12 2 3z" stroke="#555" stroke-width="1.6" fill="none"/></svg>123 -456 -7890</div>
      <div class="row"><svg width="24" height="20" viewBox="0 0 24 20"><rect x="1" y="3" width="22" height="15" stroke="#555" stroke-width="1.6" fill="none"/><path d="M1 3l11 9 11-9" stroke="#555" stroke-width="1.6" fill="none"/></svg>info@northfieldstudio-example.com</div>
      <div class="row"><svg width="22" height="26" viewBox="0 0 22 26"><path d="M11 2a8 8 0 0 0-8 8c0 6 8 14 8 14s8-8 8-14a8 8 0 0 0-8-8z" stroke="#555" stroke-width="1.6" fill="none"/><circle cx="11" cy="10" r="3" stroke="#555" stroke-width="1.6" fill="none"/></svg>18 Alder Lane<br>Eastbrook, CT 06000</div>
    </div>
    <div class="form">
      <div>Name</div><div>Email</div><div class="msg">Message</div>
      <span class="send">SEND</span>
    </div>
  </div>
</div></section>
<footer class="footer">
  <p class="copy">© Northfield Studio 2017</p>
  <div class="links"><span>Disclaimer</span><span>Careers</span><span>News</span><span>Contact Us</span></div>
  <div class="icons"><i></i><i></i><i></i><i></i></div>
</footer>
</body>
</html>
```